Roof Plumbing Company needs simple, modern business card using the attached logo and below details:

Dean Halloway
Summit Gutters Pty Ltd
ABN: 58 214 937 062
Phone: 0417 286 531
Email: summitgutters@mailbrook.com
Website: summitgutters.com.au

For all of your metal roof plumbing requirements contact Summit Gutters for an obligation free quote - no job too big or to small!

Industry/Entity Type

Business

Contact Information for Business Card

Dean Halloway
Summit Gutters Pty Ltd
ABN 58 214 937 062
0417 286 531
summitgutters@mailbrook.com
summitgutters.com.au

Requirements
Must have
• Bright eye catching design, professional look

```html
<!DOCTYPE html>
<html lang="en">
<head>
<meta charset="utf-8">
<title>Summit Gutters – Business Card</title>
<link href="https://fonts.googleapis.com/css2?family=Montserrat:wght@500;700&family=Open+Sans:wght@400&display=swap" rel="stylesheet">
<style>
  :root {
    --bg: #e6e4e5;
    --card: #ffffff;
    --red: #d62a2a;
    --red-dark: #9e2a2a;
    --strip: #4a4a4c;
    --ink: #3d3d3f;
    --muted: #555558;
  }
  * { margin: 0; padding: 0; box-sizing: border-box; }
  html, body { width: 1200px; height: 1200px; overflow: hidden; }
  body { background: var(--bg); position: relative; font-family: "Open Sans", sans-serif; }

  .card {
    position: absolute;
    width: 712px; height: 419px;
    background: var(--card);
    border-radius: 22px;
    overflow: hidden;
  }
  .card--front { left: 238px; top: 118px; }
  .card--back { left: 230px; top: 643px; }

  .wordmark {
    position: absolute;
    display: flex; align-items: center; gap: 14px;
    font-family: "Montserrat", sans-serif;
    font-weight: 700;
    color: var(--red);
    letter-spacing: 2px;
    text-transform: uppercase;
    white-space: nowrap;
  }
  .wordmark__square { width: 26px; height: 26px; background: var(--red); flex: none; }
  .card--front .wordmark { left: 0; right: 0; top: 185px; justify-content: center; font-size: 38px; }
  .card--back .wordmark { left: 108px; top: 100px; font-size: 24px; gap: 10px; }
  .card--back .wordmark__square { width: 18px; height: 18px; }

  .side-band {
    position: absolute; left: 0; top: 0; bottom: 0; width: 60px;
    background: linear-gradient(180deg, var(--red) 0%, var(--red-dark) 100%);
  }
  .side-strip {
    position: absolute; left: 60px; top: 0; bottom: 0; width: 8px;
    background: var(--strip);
  }

  .abn {
    position: absolute; right: 42px; top: 171px;
    font-size: 16px; color: var(--ink);
  }

  .contact-list {
    position: absolute; left: 104px; top: 299px;
    list-style: none;
    font-size: 17px; color: var(--ink);
  }
  .contact-list li { display: flex; align-items: center; gap: 14px; height: 24.5px; }
  .contact-list svg { width: 16px; height: 16px; flex: none; }

  .person { position: absolute; right: 42px; top: 296px; text-align: right; }
  .person__name {
    font-family: "Montserrat", sans-serif; font-weight: 500;
    font-size: 27px; color: var(--red); letter-spacing: 0.5px;
  }
  .person__role { font-size: 15px; color: var(--ink); margin-top: 6px; }
</style>
</head>
<body>

<section class="card card--front">
  <div class="wordmark"><span class="wordmark__square"></span>Summit Gutters Pty Ltd</div>
</section>

<section class="card card--back">
  <div class="side-band"></div>
  <div class="side-strip"></div>

  <div class="wordmark"><span class="wordmark__square"></span>Summit Gutters Pty Ltd</div>

  <p class="abn">ABN 58 214 937 062</p>

  <ul class="contact-list">
    <li>
      <svg viewBox="0 0 16 16" aria-hidden="true"><path fill="#d62a2a" d="M2 5c0-2 3-3 6-3s6 1 6 3v1h-3V5H5v1H2zM4 7h8l2 7H2zM8 9a2 2 0 1 0 0 4 2 2 0 0 0 0-4z"/></svg>
      0417 286 531
    </li>
    <li>
      <svg viewBox="0 0 16 16" aria-hidden="true"><g fill="none" stroke="#d62a2a" stroke-width="1.5"><circle cx="8" cy="8" r="6.5"/><ellipse cx="8" cy="8" rx="2.8" ry="6.5"/><path d="M1.5 8h13M3 4.5h10M3 11.5h10"/></g></svg>
      summitgutters.com.au
    </li>
    <li>
      <svg viewBox="0 0 16 16" aria-hidden="true"><rect x="1" y="3" width="14" height="10" fill="#d62a2a"/><path d="M1 3l7 6 7-6" fill="none" stroke="#fff" stroke-width="1.3"/></svg>
      summitgutters@mailbrook.com
    </li>
  </ul>

  <div class="person">
    <p class="person__name">Dean Halloway</p>
    <p class="person__role">Director</p>
  </div>
</section>

</body>
</html>
```